Corvane spray foam and Environmental

I have business cards but need new ones. The ones I have are very bland. Here is. Y company website http://www.corvanesprayfoam.ca

Also I can send you copies of the current cards
I would also need my current logo on the new design as well.. Also spray foam and Environmental

Industry/Entity Type

Business

Logo Text

Corvane.

```html
<!DOCTYPE html>
<html lang="en">
<head>
<meta charset="utf-8">
<title>Corvane Business Card</title>
<link rel="stylesheet" href="https://fonts.googleapis.com/css2?family=Roboto:wght@400;500;700&family=Roboto+Condensed:wght@700&display=swap">
<style>
  :root {
    --page-bg: #e6e6e8;
    --card-dark: #1e1e20;
    --card-light: #f7f7f7;
    --purple: #7a2f91;
    --purple-deep: #5a2170;
    --text-light: #ffffff;
    --text-grey: #555555;
    --divider: #b9b9b9;
    --mark-grey: #8a8d94;
  }
  * { box-sizing: border-box; margin: 0; padding: 0; }
  html, body { width: 1200px; height: 900px; overflow: hidden; }
  body {
    background: var(--page-bg);
    font-family: "Roboto", Arial, sans-serif;
    position: relative;
  }
  .card {
    position: absolute;
    left: 320px;
    width: 560px;
    height: 320px;
    box-shadow: 0 6px 18px rgba(0,0,0,0.18);
  }
  .card-front {
    top: 100px;
    background: var(--card-dark);
    color: var(--text-light);
    text-align: center;
    padding-top: 28px;
  }
  .brand-square {
    width: 58px;
    height: 58px;
    margin: 0 auto 6px;
    background: var(--mark-grey);
  }
  .brand-name {
    font-weight: 700;
    font-size: 50px;
    letter-spacing: 1px;
    color: var(--purple);
    line-height: 1;
  }
  .service-heading {
    color: var(--purple);
    font-weight: 700;
    font-size: 17px;
    margin-top: 6px;
  }
  .service-list {
    font-size: 14px;
    font-weight: 500;
    line-height: 1.2;
  }
  .card-back {
    top: 480px;
    background: var(--card-light);
  }
  .person {
    position: absolute;
    left: 0;
    top: 128px;
    width: 250px;
    text-align: right;
    padding-right: 28px;
  }
  .person-name {
    font-family: "Roboto Condensed", "Arial Narrow", sans-serif;
    font-weight: 700;
    font-size: 34px;
    color: var(--purple-deep);
    line-height: 1;
  }
  .person-title {
    font-size: 15px;
    color: var(--text-grey);
    margin-top: 4px;
    padding-right: 8px;
  }
  .divider {
    position: absolute;
    left: 262px;
    top: 40px;
    width: 1px;
    height: 240px;
    background: linear-gradient(to bottom, transparent, var(--divider) 20%, var(--divider) 80%, transparent);
  }
  .contacts {
    position: absolute;
    left: 290px;
    top: 34px;
  }
  .contact-group + .contact-group { margin-top: 18px; }
  .contact-heading {
    color: var(--purple-deep);
    font-weight: 700;
    font-size: 21px;
    margin-bottom: 6px;
  }
  .contact-line {
    display: flex;
    align-items: center;
    gap: 8px;
    font-size: 16px;
    color: var(--text-grey);
    line-height: 21px;
  }
  .contact-line svg { width: 14px; height: 14px; fill: var(--purple-deep); flex: none; }
</style>
</head>
<body>
  <section class="card card-front">
    <div class="brand-square"></div>
    <div class="brand-name">CORVANE</div>
    <div class="service-heading">Spray foam4</div>
    <p class="service-list">Roofing Foam, Slabjacking, 2 pound / Half pound<br>Sound , Proofing, Batt insulation, Attic Blow in</p>
    <div class="service-heading">Environmental</div>
    <p class="service-list">air monitoring, Asbestos testing, Asbestos Removal<br>Building Demolition, Lead Testing, Mould Removal</p>
  </section>

  <section class="card card-back">
    <div class="person">
      <div class="person-name">DANA KELLER</div>
      <div class="person-title">CEO/FOUNDER</div>
    </div>
    <div class="divider"></div>
    <div class="contacts">
      <div class="contact-group">
        <div class="contact-heading">Spray foam</div>
        <div class="contact-line"><svg viewBox="0 0 24 24"><path d="M6.6 10.8a15 15 0 0 0 6.6 6.6l2.2-2.2a1 1 0 0 1 1-.25 11.4 11.4 0 0 0 3.6.57 1 1 0 0 1 1 1V20a1 1 0 0 1-1 1A17 17 0 0 1 3 4a1 1 0 0 1 1-1h3.5a1 1 0 0 1 1 1c0 1.25.2 2.45.57 3.6a1 1 0 0 1-.25 1z"/></svg>604-555-0142</div>
        <div class="contact-line"><svg viewBox="0 0 24 24"><path d="M2 5h20v14H2z M2 5l10 8 10-8" /></svg>corvanefoam@mailbox.ca</div>
        <div class="contact-line"><svg viewBox="0 0 24 24"><circle cx="12" cy="12" r="10"/></svg>www.corvanesprayfoam.ca</div>
      </div>
      <div class="contact-group">
        <div class="contact-heading">Environmental</div>
        <div class="contact-line"><svg viewBox="0 0 24 24"><path d="M6.6 10.8a15 15 0 0 0 6.6 6.6l2.2-2.2a1 1 0 0 1 1-.25 11.4 11.4 0 0 0 3.6.57 1 1 0 0 1 1 1V20a1 1 0 0 1-1 1A17 17 0 0 1 3 4a1 1 0 0 1 1-1h3.5a1 1 0 0 1 1 1c0 1.25.2 2.45.57 3.6a1 1 0 0 1-.25 1z"/></svg>604-555-0187</div>
        <div class="contact-line"><svg viewBox="0 0 24 24"><path d="M2 5h20v14H2z M2 5l10 8 10-8" /></svg>enviro1@mailbox.ca</div>
        <div class="contact-line"><svg viewBox="0 0 24 24"><circle cx="12" cy="12" r="10"/></svg>corvaneenvironmental.ca</div>
      </div>
    </div>
  </section>
</body>
</html>
```